lawn sign

Lawn Sign
Roofing Gutters Windows

Target Market(s)

roofing

Font styles to use
Sans Serif

Colors
86cfc6
33a6d7
fbee3f
faa54b

Requirements
Must have
• my logo
Nice to have
• designer for now

```html
<!DOCTYPE html>
<html lang="en">
<head>
<meta charset="utf-8">
<title>Harlow Restoration Lawn Sign</title>
<link rel="stylesheet" href="https://fonts.googleapis.com/css2?family=Cinzel:wght@400;600;700;800&display=swap">
<style>
  :root{
    --page:#e9ece6;
    --sign:#f6f6f6;
    --green-light:#8cc63f;
    --green:#3aa14a;
    --green-deep:#12904a;
    --blue:#2583c2;
    --navy:#17386b;
    --teal:#1b8a8c;
    --ink:#1f1f1f;
    --white:#ffffff;
  }
  *{box-sizing:border-box;margin:0;padding:0}
  html,body{width:1200px;height:1200px;overflow:hidden}
  body{background:var(--page);font-family:"Cinzel",serif;position:relative}
  .sign{position:absolute;left:0;top:150px;width:1200px;height:900px;background:var(--sign);overflow:hidden}

  .offer-panel{position:absolute;left:0;top:0;width:1200px;height:440px;
    clip-path:polygon(560px 0,1200px 0,1200px 440px,750px 440px);}
  .offer-warranty{position:absolute;left:0;top:0;width:100%;height:250px;
    background:linear-gradient(90deg,var(--green-light) 45%,var(--green-deep));}
  .offer-emergency{position:absolute;left:0;top:250px;width:100%;height:140px;
    background:linear-gradient(180deg,var(--blue),var(--navy));}
  .offer-strip{position:absolute;left:0;top:390px;width:100%;height:50px;background:var(--green-light)}

  .warranty-text,.emergency-text{position:absolute;left:748px;color:var(--white);line-height:1;white-space:nowrap}
  .warranty-text{top:58px}
  .warranty-years{display:block;font-size:82px;font-weight:700}
  .warranty-years small{font-size:46px;font-weight:400;margin-left:12px}
  .warranty-word{display:block;font-size:50px;font-weight:800;margin-top:8px}
  .emergency-text{top:276px}
  .emergency-word{display:block;font-size:54px;font-weight:800}
  .emergency-sub{display:block;font-size:30px;font-weight:400;margin-top:12px}

  .brand{position:absolute;left:70px;top:200px;display:flex;align-items:center;gap:30px}
  .brand-mark{width:120px;height:120px;border-radius:50%;background:var(--teal);flex:none}
  .brand-name{color:var(--teal);font-size:34px;font-weight:600;line-height:1.25;max-width:420px}

  .services{position:absolute;left:0;top:460px;width:1200px;display:flex;justify-content:space-around;padding:0 60px}
  .service{display:flex;flex-direction:column;align-items:center;gap:22px;width:300px}
  .service-icon{width:140px;height:140px;border-radius:50%;background:var(--green-light);border:5px solid var(--navy);display:flex;align-items:center;justify-content:center}
  .service-label{font-size:50px;font-weight:800;color:var(--ink);white-space:nowrap}

  .contact-band{position:absolute;left:0;top:790px;width:1200px;height:110px;
    background:linear-gradient(180deg,var(--blue),var(--navy));display:flex;align-items:flex-end;justify-content:center;padding-bottom:14px}
  .contact-phone{color:var(--white);font-size:56px;font-weight:800;letter-spacing:1px;line-height:1;white-space:nowrap}
  .web-pill{position:absolute;left:320px;top:755px;width:560px;height:62px;border-radius:31px;
    background:linear-gradient(90deg,var(--green-light),var(--green-deep));display:flex;align-items:center;justify-content:center;
    color:var(--white);font-size:32px;font-weight:800;white-space:nowrap}
</style>
</head>
<body>
<main class="sign">
  <section class="offer-panel">
    <div class="offer-warranty"></div>
    <div class="offer-emergency"></div>
    <div class="offer-strip"></div>
  </section>
  <div class="warranty-text">
    <span class="warranty-years">30-50<small>YEAR</small></span>
    <span class="warranty-word">WARRANTIES</span>
  </div>
  <div class="emergency-text">
    <span class="emergency-word">EMERGENCY</span>
    <span class="emergency-sub">SERVICES AVAILABLE</span>
  </div>

  <div class="brand">
    <span class="brand-mark"></span>
    <span class="brand-name">HARLOW RESTORATION REMODELING GROUP LLC</span>
  </div>

  <section class="services">
    <div class="service">
      <div class="service-icon">
        <svg width="80" height="80" viewBox="0 0 80 80" fill="none" stroke="#fff" stroke-width="6" stroke-linejoin="round">
          <path d="M8 40 L40 12 L72 40"/><path d="M18 34 V70 H34 V50 H46 V70 H62 V34"/>
        </svg>
      </div>
      <span class="service-label">ROOFING</span>
    </div>
    <div class="service">
      <div class="service-icon">
        <svg width="80" height="80" viewBox="0 0 80 80" fill="none" stroke="#fff" stroke-width="5">
          <rect x="10" y="12" width="60" height="56"/><line x1="40" y1="12" x2="40" y2="68"/><line x1="10" y1="40" x2="70" y2="40"/>
        </svg>
      </div>
      <span class="service-label">WINDOWS</span>
    </div>
    <div class="service">
      <div class="service-icon">
        <svg width="80" height="80" viewBox="0 0 80 80" fill="none" stroke="#fff" stroke-width="5" stroke-linejoin="round">
          <path d="M8 28 H64 V40 H8 Z"/><path d="M44 40 V68 H56 V40"/>
        </svg>
      </div>
      <span class="service-label">GUTTERS</span>
    </div>
  </section>

  <div class="contact-band"><span class="contact-phone">CALL US: (555) 014-2287</span></div>
  <div class="web-pill">WWW.HARLOWLLC.COM</div>
</main>
</body>
</html>
```